Web Design Project for Industrial Hemp

I'm launching a new company to grow Industrial Hemp and then to set up a manufacturing facility to process the crop each and every year. We require a complete end to end brand and livery suite and we will start with a web presence. We want to appeal to (a) Investors, Employees, Farmers, and consumers so as to engage with all our stakeholders. We want to create a whole new industry that becomes a game changer for environmentally friendly crop production. Hemp is gaining in popularity and credibility across the world!

Target Market(s)

Farmers to produce, Manufacturers who will purchase the raw materials, Investors who will invest in the project, Consumers who will buy Hemp Products

Industry/Entity Type

Industry

Requirements
Must have
• Environmentally Friendly
Carbon Neutral/Positive
Game Changer
Multi-Use Crop
50,000 products can be made from Hemp
Should not have
• Should avoid its relationship with cannabis but not ignore it! When the regulatory bodies acknowledge the benefits of cannabanoids, they will start to legalise the production of cannabis for sale on prescription

```html
<!DOCTYPE html>
<html lang="en">
<head>
<meta charset="utf-8">
<title>Greenfield Fibre Works Ltd</title>
<link href="https://fonts.googleapis.com/css2?family=Bebas+Neue&family=Open+Sans:wght@400;600;700&family=Arimo:wght@400&display=swap" rel="stylesheet">
<style>
:root{
  --green:#6aaf3d;
  --green-light:#79b843;
  --green-dark:#3f7d1f;
  --green-deep:#2f6417;
  --green-field:#5c9a2f;
  --ink:#222;
  --grey-text:#666;
  --grey-band:#ededed;
  --grey-btn:#6f6f6f;
  --frame:#a9a9a9;
  --slide-fill:#8a8f88;
  --yellow:#f2dc2a;
  --white:#fff;
}
*{margin:0;padding:0;box-sizing:border-box}
html,body{width:1200px;height:4186px;overflow:hidden;background:var(--white)}
body{position:relative;font-family:"Open Sans",Arial,sans-serif;color:var(--ink)}
.abs{position:absolute}
.center{text-align:center}
.display{font-family:"Bebas Neue",Impact,sans-serif;letter-spacing:1px}

/* nav */
.site-nav{left:0;top:0;width:1200px;height:105px;background:linear-gradient(var(--green-light),var(--green-dark));}
.site-nav ul{list-style:none;display:flex;justify-content:center;gap:20px;padding-top:50px}
.site-nav li{font-family:"Bebas Neue",Impact,sans-serif;font-size:22px;color:var(--white);letter-spacing:1px}
.site-nav li.active{color:#cfe7a8}
.nav-notch{left:588px;top:105px;width:0;height:0;border-left:12px solid transparent;border-right:12px solid transparent;border-top:12px solid var(--green-dark)}

.shadow-curve{left:100px;width:1000px;height:40px;border-radius:50%;box-shadow:0 18px 22px -14px rgba(0,0,0,.35)}

/* hero */
.brand-title{left:0;width:1200px;top:176px;font-family:"Arimo",Arial,sans-serif;font-size:58px;color:#333}
.divider{left:540px;width:120px;height:1px;background:#bbb}
.divider::after{content:"";position:absolute;left:56px;top:-4px;width:8px;height:8px;border-radius:50%;background:var(--green)}
.tagline{left:0;width:1200px;font-size:20px;color:#333}

/* services */
.service{width:300px;text-align:center}
.service-badge{width:160px;height:160px;border-radius:50%;background:var(--green);margin:0 auto;display:flex;align-items:center;justify-content:center}
.service-badge span{width:118px;height:118px;border-radius:50%;background:#2d2d2d;border:6px solid #8fd05a;display:flex;align-items:center;justify-content:center}
.service h3{font-size:22px;font-weight:700;margin-top:32px}
.service p{font-size:13px;color:var(--grey-text);line-height:19px;margin:12px auto 0;width:230px}
.btn{display:inline-block;margin-top:20px;width:98px;height:32px;line-height:32px;font-size:11px;font-weight:700;color:var(--white);background:var(--grey-btn);border-radius:3px}
.btn.primary{background:var(--green)}

/* feature band */
.feature-band{left:98px;top:820px;width:1005px;height:157px;background:var(--grey-band);border-bottom:7px solid var(--green)}
.band-notch{left:588px;top:977px;border-left:12px solid transparent;border-right:12px solid transparent;border-top:12px solid var(--green)}
.feature{top:28px;width:235px}
.feature-icon{display:inline-block;width:48px;height:48px;border-radius:50%;background:#2d2d2d;vertical-align:middle}
.feature-icon.lit{background:var(--green)}
.feature h4{display:inline-block;vertical-align:middle;margin-left:10px;font-size:13px;font-weight:700}
.feature p{font-size:12px;color:var(--grey-text);line-height:18px;margin-top:14px}

/* section heads */
.section-title{left:0;width:1200px;font-family:"Bebas Neue",Impact,sans-serif;font-size:58px;color:#222}
.section-sub{left:0;width:1200px;font-size:20px}
.section-lede{left:290px;width:620px;font-family:"Bebas Neue",Impact,sans-serif;font-size:18px;line-height:24px}

/* portfolio */
.slider-frame{left:133px;top:1375px;width:938px;height:447px;background:var(--frame);border-radius:10px}
.slide{left:157px;top:1382px;width:883px;height:433px;background:var(--slide-fill)}
.dots{left:528px;top:1840px;display:flex;gap:12px}
.dots i{display:block;width:45px;height:8px;border-radius:4px;background:#333}
.dots i.on{background:var(--green)}

/* team */
.member{width:230px;text-align:center}
.avatar{width:180px;height:180px;border-radius:50%;background:#eceef2;margin:0 auto}
.member h4{font-size:17px;font-weight:700;margin-top:36px}
.member .role{font-size:10px;color:#888;margin-top:2px}
.member p{font-size:11.5px;color:var(--grey-text);line-height:17px;margin-top:8px}
.socials{display:flex;justify-content:center;gap:8px;margin-top:12px}
.socials i{display:block;width:20px;height:20px;border-radius:50%}
.s1{background:#36a9e1}.s2{background:#3b5b98}.s3{background:#e47f1b}.s4{background:#4a8a3a}.s5{background:#d9456e}

/* newsletter */
.newsletter{left:0;top:2722px;width:1200px;height:182px;background:var(--green-deep)}
.newsletter h5{position:absolute;left:0;width:1200px;top:58px;font-family:"Bebas Neue",Impact,sans-serif;font-size:25px;color:var(--white);font-weight:400;text-align:center}
.newsletter h6{position:absolute;left:0;width:1200px;top:90px;font-family:"Bebas Neue",Impact,sans-serif;font-size:22px;color:var(--yellow);font-weight:400;text-align:center}
.subscribe{left:420px;top:138px;width:380px;height:38px;background:#8dc65a;border-radius:3px;padding:4px}
.subscribe .field{position:absolute;left:4px;top:4px;width:280px;height:30px;background:var(--white);font-size:12px;color:#999;line-height:30px;padding-left:42px}
.subscribe .field::before{content:"";position:absolute;left:10px;top:8px;width:22px;height:14px;background:var(--green)}
.subscribe .go{position:absolute;right:4px;top:4px;width:86px;height:30px;background:var(--green);font-size:11px;font-weight:700;color:var(--white);text-align:center;line-height:30px}

/* contact */
.contact{left:0;top:2995px;width:1200px;height:949px;background:linear-gradient(var(--green-light),var(--green))}
.contact .section-title,.contact .section-sub,.contact .section-lede{color:var(--white)}
.col-head{font-family:"Bebas Neue",Impact,sans-serif;font-size:22px;color:var(--white)}
.send-copy{left:133px;top:3490px;width:620px;font-size:12px;line-height:19px;color:var(--white);text-align:center}
.input{top:3605px;height:32px;background:var(--green-field);border:1px solid #4d8a25;font-size:11px;color:#d8edc3;padding:8px 12px}
.textarea{left:133px;top:3657px;width:617px;height:147px;background:var(--green-field);border:1px solid #4d8a25;font-size:11px;color:#d8edc3;padding:10px 12px}
.send-btn{left:150px;top:3755px;width:84px;height:84px;border-radius:50%;background:var(--green-deep);border:6px solid #93cd60;display:flex;align-items:center;justify-content:center}
.globe{left:796px;top:3473px;width:290px;height:290px;border-radius:50%;background:radial-gradient(circle at 40% 40%,#6ea844,#4a8526)}
.address{left:866px;top:3665px;width:209px;height:52px;background:var(--yellow);font-size:11px;line-height:17px;padding:8px 10px 0 40px;color:#333}
.pin{left:812px;top:3662px}
.info{left:866px;top:3752px;font-size:12px;line-height:21px;color:var(--white)}

/* footer */
.to-top{left:565px;top:3980px;width:70px;height:70px;border-radius:50%;background:var(--green-deep);border:5px solid var(--green);display:flex;align-items:center;justify-content:center}
.copyright{left:0;width:1200px;top:4070px;font-size:16px;line-height:23px;text-align:center;color:#222}
</style>
</head>
<body>

<nav class="abs site-nav">
  <ul>
    <li>Home.</li><li class="active">Services.</li><li>About.</li><li>Portfolio.</li><li>Blog.</li><li>Contact.</li>
  </ul>
</nav>
<div class="abs nav-notch"></div>
<div class="abs shadow-curve" style="top:70px"></div>

<header>
  <h1 class="abs brand-title center" style="font-weight:400">Greenfield Fibre Works Ltd</h1>
  <div class="abs divider" style="top:262px"></div>
  <p class="abs tagline center" style="top:272px">Your Great Services</p>
</header>

<section class="services">
  <div class="abs service" style="left:154px;top:385px">
    <div class="service-badge"><span>
      <svg width="44" height="54" viewBox="0 0 44 54"><path d="M15 2h14M18 2v18L4 48a3 3 0 0 0 3 4h30a3 3 0 0 0 3-4L26 20V2" fill="none" stroke="#8fd05a" stroke-width="4"/></svg>
    </span></div>
    <h3>LOREM IMPOSIUM</h3>
    <p>Grown in open fields with no sprays, our crop puts more carbon back into the soil than it takes out.</p>
    <a class="btn">READ MORE</a>
  </div>
  <div class="abs service" style="left:450px;top:385px">
    <div class="service-badge"><span>
      <svg width="40" height="54" viewBox="0 0 40 54"><path d="M20 52V14M20 30c-10 0-16-8-16-16 10 0 16 6 16 16zM20 24c8 0 14-6 14-14-8 0-14 6-14 14z" fill="#8fd05a"/></svg>
    </span></div>
    <h3>LOREM IMPOSIUM</h3>
    <p>One field gives fibre, oil and seed, feeding thousands of everyday goods from rope to building block.</p>
    <a class="btn primary">READ MORE</a>
  </div>
  <div class="abs service" style="left:750px;top:385px">
    <div class="service-badge"><span>
      <svg width="44" height="50" viewBox="0 0 44 50"><circle cx="22" cy="14" r="11" fill="#8fd05a"/><path d="M2 50c0-14 9-22 20-22s20 8 20 22z" fill="#8fd05a"/></svg>
    </span></div>
    <h3>LOREMIMPOSIUM</h3>
    <p>Farmers, makers and investors work as one to build a cleaner industry from the ground up each year.</p>
    <a class="btn">READ MORE</a>
  </div>
</section>

<section class="abs feature-band">
  <div class="abs feature" style="left:30px"><span class="feature-icon lit"></span><h4>DINING IDEAS</h4><p>Hemp seed and oil bring rich, clean protein to the kitchen table.</p></div>
  <div class="abs feature" style="left:275px"><span class="feature-icon"></span><h4>DESIGN THERAPY</h4><p>Strong natural fibre shapes cloth, board and paper for makers.</p></div>
  <div class="abs feature" style="left:520px"><span class="feature-icon"></span><h4>ONLINE SUPPORT</h4><p>Our team helps growers plan, plant and sell every single season.</p></div>
  <div class="abs feature" style="left:765px"><span class="feature-icon"></span><h4>RESPONSIVE DESIGN</h4><p>Crops fit local soils and climates with very little water used.</p></div>
</section>
<div class="abs band-notch"></div>
<div class="abs shadow-curve" style="top:955px"></div>

<section class="portfolio">
  <h2 class="abs section-title center display" style="top:1120px;font-weight:400">Portfolio</h2>
  <div class="abs divider" style="top:1200px"></div>
  <p class="abs section-sub center" style="top:1208px">We are Green Creatives</p>
  <p class="abs section-lede center" style="top:1270px">Loremipsumdolor slo donsec tueraliquet morbi necin curabitur lreaoreet nisl loremin pellente e vidicus pannel impirus saohntas</p>
  <div class="abs slider-frame"></div>
  <div class="abs slide" role="img" aria-label="Portfolio slide photograph: hillside field above a coastal bay"></div>
  <div class="abs dots"><i></i><i class="on"></i><i></i></div>
</section>

<section class="about">
  <h2 class="abs section-title center" style="top:1996px;font-weight:400">About Us</h2>
  <div class="abs divider" style="top:2076px"></div>
  <p class="abs section-sub center" style="top:2084px">We are Green Creatives</p>
  <p class="abs section-lede center" style="top:2143px">Lorem ipsum dolor slo donsec tueraliquet morbi necin curabitur lreaoreet nisl lorem in pellente e vidicus pannel impirus saohntas</p>

  <div class="abs member" style="left:129px;top:2251px">
    <div class="avatar" role="img" aria-label="Portrait of team member"></div>
    <h4>AARON PELL</h4><p class="role">FARM LEAD</p>
    <p>Runs our growing trials and works with local farmers on every new planting.</p>
    <div class="socials"><i class="s1"></i><i class="s2"></i><i class="s3"></i><i class="s4"></i><i class="s5"></i></div>
  </div>
  <div class="abs member" style="left:367px;top:2251px">
    <div class="avatar" role="img" aria-label="Portrait of team member"></div>
    <h4>TESSA MARLOW</h4><p class="role">MILL MANAGER</p>
    <p>Oversees the processing plant that turns each harvest into fibre and oil.</p>
    <div class="socials"><i class="s1"></i><i class="s2"></i><i class="s3"></i><i class="s4"></i><i class="s5"></i></div>
  </div>
  <div class="abs member" style="left:607px;top:2251px">
    <div class="avatar" role="img" aria-label="Portrait of team member"></div>
    <h4>VICTOR CRANE</h4><p class="role">INVESTOR RELATIONS</p>
    <p>Keeps our backers informed as the project grows from field to factory.</p>
    <div class="socials"><i class="s1"></i><i class="s2"></i><i class="s3"></i><i class="s4"></i><i class="s5"></i></div>
  </div>
  <div class="abs member" style="left:848px;top:2251px">
    <div class="avatar" role="img" aria-label="Portrait of team member"></div>
    <h4>DANA ROWLEY</h4><p class="role">PRODUCT DESIGN</p>
    <p>Develops new hemp goods for shoppers, from textiles to natural care items.</p>
    <div class="socials"><i class="s1"></i><i class="s2"></i><i class="s3"></i><i class="s4"></i><i class="s5"></i></div>
  </div>
</section>

<section class="abs newsletter">
  <h5>Get in touch with us to get the latest newsletter. to know our latest activity about the nature care.</h5>
  <h6>Dont worry! This it will be not a spam, beleive and support us!</h6>
  <div class="abs subscribe"><div class="field">Type your email...</div><div class="go">SUBSCRIBE</div></div>
</section>
<div class="abs shadow-curve" style="top:2880px"></div>

<section class="abs contact">
  <h2 class="abs section-title center" style="top:148px;font-weight:400">Contact Us</h2>
  <div class="abs divider" style="top:228px;background:#e6f3d6"></div>
  <p class="abs section-sub center" style="top:236px">We are Green Creatives</p>
  <p class="abs section-lede center" style="top:292px">Loremipsumdolor slo donsec tueraliquet morbi necin curabitur lreaoreet nisl loremin pellente e vidicus pannel impirus saohntas</p>
  <h3 class="abs col-head" style="left:133px;width:620px;top:430px;text-align:center;font-weight:400">Send &nbsp;us a mesage</h3>
  <h3 class="abs col-head" style="left:796px;width:290px;top:430px;text-align:center;font-weight:400">Contact info</h3>
</section>

<p class="abs send-copy">Tell us who you are and how you would like to take part. Farmers, makers, investors and shoppers are all welcome. Ask about planting, supply, products or our plans, and a member of our small team will reply to you within two working days.</p>
<div class="abs input" style="left:133px;width:187px">Your name...</div>
<div class="abs input" style="left:348px;width:187px">Your last name...</div>
<div class="abs input" style="left:563px;width:187px">Your Email...</div>
<div class="abs textarea">Your message...</div>
<div class="abs send-btn"><svg width="30" height="22" viewBox="0 0 30 22"><rect x="1" y="1" width="28" height="20" fill="none" stroke="#f2dc2a" stroke-width="2"/><path d="M1 1l14 11L29 1" fill="none" stroke="#f2dc2a" stroke-width="2"/></svg></div>

<div class="abs globe" role="img" aria-label="Illustration of a globe showing the world map"></div>
<svg class="abs pin" width="44" height="58" viewBox="0 0 44 58"><path d="M22 2C11 2 3 10 3 21c0 14 19 35 19 35s19-21 19-35C41 10 33 2 22 2z" fill="#fff"/><circle cx="22" cy="21" r="7" fill="#5c9a2f"/></svg>
<div class="abs address">48 Meadow Lane, Fieldtown<br>FT 20418</div>
<div class="abs info">Phone: 1-800-555-0142<br>Fax: 1-800-555-0143<br>Web: www.greenfieldfibre.example</div>
<div class="abs shadow-curve" style="top:3920px"></div>

<footer>
  <div class="abs to-top"><svg width="28" height="18" viewBox="0 0 28 18"><path d="M3 15L14 4l11 11" fill="none" stroke="#fff" stroke-width="4"/></svg></div>
  <p class="abs copyright">© 2013 GREENFIELD ALL RIGHTS RESERVED,<br>GROWN WITH CARE FOR A CLEANER FUTURE</p>
  <div class="abs socials" style="left:0;width:1200px;top:4130px"><i class="s1"></i><i class="s2"></i><i class="s3"></i><i class="s4"></i><i class="s5"></i></div>
</footer>

</body>
</html>
```